Design a Product Label for a Natural Deodorant Product

This brief is for the development of a product label for a natural deodorant product that we are creating. The requirement is for a sticker label that will be applied to the package. Full details of the project are provided in the attached briefing document.

Target Market(s)

Those seeking an alternative to chemical laden deodorants. Interested in natural products with minimal waste etc.

Industry/Entity Type

Skin Care

Requirements
Must have
• On brand. Simple.

```html
<!DOCTYPE html>
<html lang="en">
<head>
<meta charset="utf-8">
<title>Terrana Deodorant – Label</title>
<link rel="stylesheet" href="https://fonts.googleapis.com/css2?family=Cinzel:wght@400;600&display=swap">
<style>
  :root {
    --page-bg: #e6e4e2;
    --label-light: #a7a29d;
    --label-mid: #948f8a;
    --label-dark: #837d78;
    --ink: #1f1b19;
    --ink-soft: #3a3431;
    --foliage: #6f6661;
    --band: #4a423e;
    --band-text: #e9e3dd;
    --rule: #2a2421;
  }
  * { margin: 0; padding: 0; box-sizing: border-box; }
  html, body {
    width: 1200px;
    height: 1200px;
    overflow: hidden;
    background: var(--page-bg);
  }
  .canvas {
    position: relative;
    width: 1200px;
    height: 1200px;
  }
  .label {
    position: absolute;
    left: 150px;
    top: 200px;
    width: 900px;
    height: 800px;
    background: radial-gradient(ellipse at 55% 40%, var(--label-light) 0%, var(--label-mid) 55%, var(--label-dark) 100%);
    border-top: 3px solid var(--rule);
    border-bottom: 3px solid var(--rule);
    font-family: "Cinzel", serif;
    color: var(--ink);
    overflow: hidden;
  }
  .maker {
    position: absolute;
    top: 44px;
    left: 0;
    width: 100%;
    display: flex;
    justify-content: center;
    align-items: center;
    gap: 10px;
    font-size: 18px;
    font-weight: 400;
    letter-spacing: 2px;
    color: var(--ink-soft);
  }
  .maker-dot {
    width: 14px;
    height: 14px;
    border-radius: 50%;
    background: var(--ink-soft);
  }
  .product-name {
    position: absolute;
    top: 90px;
    left: 0;
    width: 100%;
    text-align: center;
    font-size: 104px;
    font-weight: 400;
    line-height: 1;
    letter-spacing: 4px;
    color: var(--ink);
  }
  .product-type {
    position: absolute;
    top: 212px;
    left: 0;
    width: 100%;
    text-align: center;
    font-size: 44px;
    font-weight: 400;
    letter-spacing: 6px;
    line-height: 1;
    color: var(--ink);
  }
  .foliage {
    position: absolute;
    left: 10px;
    top: 320px;
    width: 400px;
    height: 320px;
    border-radius: 48% 52% 40% 60% / 55% 45% 55% 45%;
    background: radial-gradient(ellipse at center, var(--foliage) 0%, rgba(111,102,97,0.55) 55%, rgba(111,102,97,0) 100%);
  }
  .scent-name {
    position: absolute;
    left: 460px;
    top: 520px;
    font-size: 34px;
    font-weight: 400;
    letter-spacing: 1px;
    color: var(--ink);
  }
  .claims {
    position: absolute;
    left: 0;
    bottom: 0;
    width: 100%;
    height: 64px;
    background: linear-gradient(to bottom, rgba(74,66,62,0.55), var(--band));
    border-top: 2px solid var(--rule);
    display: flex;
    justify-content: space-around;
    align-items: center;
    font-size: 24px;
    letter-spacing: 1px;
    color: var(--band-text);
  }
  .claims .claim-main { font-weight: 600; }
</style>
</head>
<body>
  <main class="canvas">
    <section class="label">
      <div class="maker">
        <span class="maker-dot"></span>
        <span class="maker-name">HARLOW GOODS</span>
      </div>
      <h1 class="product-name">TERRANA</h1>
      <p class="product-type">DEODORANT</p>
      <div class="foliage" role="img" aria-label="Faint botanical illustration of leafy sprigs"></div>
      <p class="scent-name">SCENT NAME</p>
      <footer class="claims">
        <span class="claim">ALL NATURAL</span>
        <span class="claim claim-main">CHEMICAL FREE</span>
        <span class="claim">DEODORANT</span>
      </footer>
    </section>
  </main>
</body>
</html>
```